Illustration Design Project

I have an existing illustration I have written up, I need it professionally redone, perhaps as an infographic or new design from the current layout.

Pls plan for a few edits and revisions.

I will need it large enough to be made into a wall poster size.

```html
<!DOCTYPE html>
<html lang="en">
<head>
<meta charset="utf-8">
<title>Accountability / Complacency</title>
<link rel="stylesheet" href="https://fonts.googleapis.com/css2?family=Archivo:ital,wght@0,400;0,700;0,800;0,900;1,400&display=swap">
<style>
  :root {
    --ink: #1c1a1b;
    --paper: #ffffff;
  }
  * { margin: 0; padding: 0; box-sizing: border-box; }
  html, body { width: 800px; height: 1200px; overflow: hidden; background: var(--ink); }
  .poster {
    position: relative;
    width: 800px;
    height: 1200px;
    background: var(--ink);
    font-family: "Archivo", "Helvetica Neue", Arial, sans-serif;
    color: var(--ink);
  }
  .panel {
    position: absolute;
    left: 24px; top: 100px;
    width: 752px; height: 1076px;
    background: var(--paper);
  }
  .art { position: absolute; left: 0; top: 0; width: 800px; height: 1200px; }
  .art text { font-family: "Archivo", "Helvetica Neue", Arial, sans-serif; font-weight: 800; }
  .title-text { fill: var(--paper); font-size: 38px; }
  .heading { fill: var(--ink); font-size: 74px; }

  .step {
    position: absolute;
    left: 0; width: 800px; height: 34px;
  }
  .step-label {
    position: absolute;
    right: 438px;
    top: 50%;
    transform: translateY(-50%);
    text-align: right;
    font-weight: 700;
    font-size: 17px;
    line-height: 1.2;
    white-space: nowrap;
  }
  .step-number {
    position: absolute;
    left: 373px; top: 0;
    width: 28px; height: 34px;
    background: var(--ink);
    color: var(--paper);
    font-size: 21px;
    font-weight: 400;
    display: flex; align-items: center; justify-content: center;
  }
  .step-quote {
    position: absolute;
    left: 423px;
    top: 50%;
    transform: translateY(-50%);
    font-style: italic;
    font-size: 15px;
    line-height: 1.2;
    letter-spacing: -0.2px;
    white-space: nowrap;
  }
</style>
</head>
<body>
<main class="poster">
  <div class="panel"></div>

  <svg class="art" viewBox="0 0 800 1200" role="img" aria-label="Accountability versus complacency ladder">
    <title>Accountability / Complacency</title>
    <text class="title-text" x="33" y="49" textLength="367" lengthAdjust="spacingAndGlyphs">ACCOUNTABILITY</text>
    <polygon points="402,68 410,68 433,12 425,12" fill="#ffffff"/>
    <text class="title-text" x="431" y="80" textLength="340" lengthAdjust="spacingAndGlyphs">COMPLACENCY</text>

    <g fill="none" stroke="#1c1a1b" stroke-width="7" stroke-dasharray="5 4">
      <path d="M160 637 H84 V187 H124"/>
      <path d="M656 637 H707 V1097 H508"/>
    </g>
    <polygon points="123,166 149,187 123,208" fill="#1c1a1b"/>
    <polygon points="629,637 656,615 656,659" fill="#1c1a1b"/>

    <text class="heading" x="156" y="211" textLength="473" lengthAdjust="spacingAndGlyphs">ACCOUNTABLE</text>
    <text class="heading" x="168" y="663" textLength="447" lengthAdjust="spacingAndGlyphs">LIFE HAPPENS</text>
    <text class="heading" x="296" y="1117" textLength="200" lengthAdjust="spacingAndGlyphs">VICTIM</text>
  </svg>

  <div class="step" style="top:248px"><span class="step-label">GETS ON WITH IT</span><span class="step-number">5</span><span class="step-quote">“OK , LET’S DO IT!”</span></div>
  <div class="step" style="top:319px"><span class="step-label">FINDS SOLUTION</span><span class="step-number">4</span><span class="step-quote">“WHAT CAN I DO?”</span></div>
  <div class="step" style="top:394px"><span class="step-label">OWNS IT</span><span class="step-number">3</span><span class="step-quote">“IF IT’S TO BE, IT’S UP TO ME!”</span></div>
  <div class="step" style="top:466px"><span class="step-label">ACKNOWLEDGES<br>REALITY</span><span class="step-number">2</span><span class="step-quote">“THIS IS THE WAY IT IS.”</span></div>
  <div class="step" style="top:539px"><span class="step-label">SEEKS REALITY</span><span class="step-number">1</span><span class="step-quote">“WHAT’S HAPPENING?”</span></div>

  <div class="step" style="top:704px"><span class="step-label">AVOIDS REALITY</span><span class="step-number">1</span><span class="step-quote">“ASK NO QUESTIONS.”</span></div>
  <div class="step" style="top:776px"><span class="step-label">FIGHTS REALITY</span><span class="step-number">2</span><span class="step-quote">“THAT’S NOT HOW I SEE IT.”</span></div>
  <div class="step" style="top:850px"><span class="step-label">BLAMES</span><span class="step-number">3</span><span class="step-quote">“IF EVERYONE WOULD JUST<br>DO THEIR JOB!”</span></div>
  <div class="step" style="top:920px"><span class="step-label">PERSONAL EXCUSES</span><span class="step-number">4</span><span class="step-quote">“IT’S NOT MY JOB.”</span></div>
  <div class="step" style="top:994px"><span class="step-label">WAITS AND HOPES</span><span class="step-number">5</span><span class="step-quote">“IF IT WAS MEANT TO BE,<br>IT WILLL HAPPEN.”</span></div>
</main>
</body>
</html>
```